American cannabis tech company business card design

Quillo.com is seeking a modern, professional, and brand-aligned business card that represents our company and its core values: Mission, Story, Values, and Impact. As an innovative cannabis company, we want a business card that is not only visually appealing but also serves as a representation of who we are and what we stand for.

Project Scope: Design a double-sided business card that integrates our brand identity and core values. Incorporate our key brand elements, ensuring a sleek and contemporary aesthetic. Visually reflect our core values (Mission, Story, Values, Impact) in a way that is engaging yet professional.

Target Market(s)

Vendors, third parties,

Contact Information for Business Card

Contact details (name, title, email, phone, website, etc.)

Font styles to use
Other font styles liked:
• Caslon, Centra

Colors

Designer to choose colors to be used in the design.

Requirements
Must have
• Quillo.com logo and branding A creative yet clean way to integrate our core values (Mission, Story, Values, Impact) Modern typography and a well-structured layout
Nice to have
• forest green, grey, white, black
Should not have
• references to marijuana, leafs, plants, or related product

```html
<!DOCTYPE html>
<html lang="en">
<head>
<meta charset="utf-8">
<title>Quillo.com Business Card</title>
<link href="https://fonts.googleapis.com/css2?family=Libre+Caslon+Text:wght@400;700&display=swap" rel="stylesheet">
<style>
  :root {
    --forest: #16301a;
    --ink-grey: #4a4a4a;
    --rule-grey: #b9b9b9;
    --card-white: #ffffff;
    --backdrop: #e6e7e5;
  }
  * { margin: 0; padding: 0; box-sizing: border-box; }
  html, body {
    width: 1200px;
    height: 900px;
    overflow: hidden;
    background: var(--backdrop);
    font-family: "Libre Caslon Text", Georgia, serif;
  }
  .stage {
    width: 1200px;
    height: 900px;
    display: flex;
    flex-direction: column;
    align-items: center;
    justify-content: center;
    gap: 50px;
  }
  .card {
    position: relative;
    width: 560px;
    height: 320px;
    background: var(--card-white);
    box-shadow: 0 6px 18px rgba(0,0,0,0.18);
  }
  .wordmark {
    color: var(--forest);
    font-weight: 700;
    letter-spacing: 1px;
    line-height: 1;
  }
  .card-front {
    display: flex;
    align-items: center;
    justify-content: center;
  }
  .card-front .wordmark { font-size: 68px; }
  .card-back .wordmark {
    position: absolute;
    top: 34px;
    right: 40px;
    font-size: 54px;
  }
  .contact-block {
    position: absolute;
    left: 34px;
    right: 34px;
    bottom: 30px;
    color: var(--ink-grey);
  }
  .rule {
    height: 1px;
    background: var(--rule-grey);
  }
  .identity {
    display: flex;
    align-items: baseline;
    gap: 8px;
    padding: 12px 0 10px;
    font-size: 15px;
  }
  .person-name {
    color: var(--forest);
    font-weight: 700;
    letter-spacing: 0.5px;
  }
  .divider {
    color: var(--forest);
    font-weight: 700;
  }
  .details {
    display: flex;
    align-items: center;
    gap: 8px;
    padding-top: 10px;
    font-size: 12.5px;
  }
  .details .item {
    display: flex;
    align-items: center;
    gap: 5px;
  }
  .details .sep { color: var(--rule-grey); }
  .icon { width: 13px; height: 13px; fill: var(--forest); stroke: var(--forest); }
</style>
</head>
<body>
<main class="stage">
  <section class="card card-front">
    <span class="wordmark">QUILLO</span>
  </section>

  <section class="card card-back">
    <span class="wordmark">QUILLO</span>
    <div class="contact-block">
      <div class="rule"></div>
      <div class="identity">
        <span class="person-name">EVAN MARSH</span>
        <span class="divider">|</span>
        <span class="person-title">Co-founder &amp; CEO</span>
      </div>
      <div class="rule"></div>
      <div class="details">
        <span class="item">
          <svg class="icon" viewBox="0 0 16 16" aria-hidden="true"><path stroke="none" d="M3.6 1.5l2.3 2.6-1.4 1.8c.9 2 2.6 3.7 4.6 4.6l1.8-1.4 2.6 2.3-1.6 2.2C6.9 14.2 1.8 9.1 1.4 3.1z"/></svg>
          000-000-0000
        </span>
        <span class="sep">|</span>
        <span class="item">
          <svg class="icon" viewBox="0 0 16 16" aria-hidden="true"><rect x="1" y="3" width="14" height="10" stroke="none"/><path d="M1.5 3.5L8 9l6.5-5.5" fill="none" stroke="#fff" stroke-width="1.2"/></svg>
          evan@quillo.com
        </span>
        <span class="sep">|</span>
        <span class="item">
          <svg class="icon" viewBox="0 0 16 16" aria-hidden="true" fill="none" stroke-width="1.2"><circle cx="8" cy="8" r="6.5" fill="none"/><ellipse cx="8" cy="8" rx="3" ry="6.5" fill="none"/><path d="M1.5 8h13M2.5 5h11M2.5 11h11" fill="none"/></svg>
          www.quillo.com
        </span>
      </div>
    </div>
  </section>
</main>
</body>
</html>
```